Birchfall Kennels

create website page for Labrador Retriever stud dog business.

Target Market(s)

Owners looking to breed their dogs that compete in NFR/DSG hunt tests.

Industry/Entity Type

Dog Training

Logo Text

Birchfall Kennals - Stud Dogs

Number of Pages Required

1 page

Colors

Designer to choose colors to be used in the design.

Requirements
Must have
• link to or info from my dogs pedigree.
• Main dog I'm advertising. HRCH Pip's Whistle 4 Rounds MH
• http://www.fieldpupregistry.example/pedigree.asp?id=71926
• also link to gundog tallies-- for pass information.
• Can update the pictures to that actual pictures once design is complete.

```html
<!DOCTYPE html>
<html lang="en">
<head>
<meta charset="utf-8">
<title>Birchfall Kennels</title>
<link rel="stylesheet" href="https://fonts.googleapis.com/css2?family=Lato:ital,wght@0,400;0,700;0,900;1,700;1,900&display=swap">
<style>
  :root {
    --ink-navy: #06202f;
    --night: #0a0d10;
    --nav-black: #020304;
    --gold: #e3b96a;
    --gold-box: #e0bd78;
    --sky: #cde6f2;
    --pale: #d6ecf6;
    --white: #ffffff;
    --text: #0c1a22;
    --arrow: #16394a;
    --badge: #2a4d8f;
  }
  * { margin: 0; padding: 0; box-sizing: border-box; }
  html, body { width: 1200px; height: 2222px; overflow: hidden; }
  body {
    position: relative;
    font-family: "Lato", Arial, sans-serif;
    background: var(--night);
    color: var(--text);
  }
  .abs { position: absolute; }

  .top-strip { left: 0; top: 0; width: 1200px; height: 34px; background: #082230; }
  .hero {
    left: 0; top: 34px; width: 1200px; height: 376px;
    background:
      radial-gradient(ellipse 360px 260px at 600px 260px, #e8f4fb 0%, #b7d2e0 40%, rgba(120,150,165,0) 75%),
      linear-gradient(180deg, #6f8896 0%, #9ab3c1 50%, #5b7686 75%, #173447 88%, #0e2433 100%);
  }
  .brand {
    left: 0; top: 262px; width: 1200px; text-align: center;
    font-weight: 900; font-size: 46px; color: var(--nav-black); letter-spacing: 0.5px;
  }

  .main-nav {
    left: 0; top: 410px; width: 1200px; height: 58px; background: var(--nav-black);
    border-bottom: 2px solid #12232d;
  }
  .main-nav a {
    position: absolute; top: 19px; transform: translateX(-50%);
    color: var(--gold); text-decoration: none; font-weight: 700; font-size: 15.5px; letter-spacing: 0.8px;
    white-space: nowrap;
  }

  .slider { left: 0; top: 468px; width: 1200px; height: 381px; background: var(--night); }
  .slide-photo {
    left: 199px; top: 479px; width: 804px; height: 337px;
    border: 2px solid #d9a956; border-radius: 3px;
    background: linear-gradient(160deg, #b79569 0%, #8b6a4a 35%, #c9c4bd 55%, #7a5a40 80%, #a98458 100%);
  }
  .slide-arrow { top: 608px; }

  .intro { left: 0; top: 849px; width: 1200px; height: 204px; background: var(--ink-navy); text-align: center; }
  .intro-kicker { position: absolute; left: 0; width: 100%; top: 44px; color: var(--pale); font-weight: 700; font-size: 25px; letter-spacing: 1.5px; }
  .intro-title { position: absolute; left: 0; width: 100%; top: 80px; color: var(--gold); font-weight: 900; font-style: italic; font-size: 41px; }
  .intro-note { position: absolute; left: 0; width: 100%; top: 145px; color: var(--pale); font-weight: 700; font-style: italic; font-size: 14px; }

  .content { left: 0; top: 1053px; width: 1200px; height: 842px; background: var(--sky); }

  .sidebar {
    left: 120px; top: 1130px; width: 225px; height: 692px; background: var(--ink-navy);
    box-shadow: 5px 6px 6px rgba(0,0,0,0.35);
  }
  .sidebar-title { position: absolute; left: 0; width: 100%; top: 22px; text-align: center; color: var(--pale); font-weight: 900; font-size: 19px; letter-spacing: 0.3px; }
  .announcements {
    position: absolute; left: 12px; top: 58px; width: 201px; height: 233px; background: var(--gold-box);
    padding: 6px 7px; font-weight: 700; font-size: 14.5px; line-height: 1.28; color: #111;
  }
  .announcements p { margin-bottom: 19px; }
  .contact-art {
    position: absolute; left: 47px; top: 329px; width: 128px; height: 82px;
    background: radial-gradient(ellipse at center, #2c4654 0%, rgba(6,32,47,0) 70%);
  }
  .contact-link { position: absolute; left: 0; width: 100%; top: 356px; text-align: center; color: var(--white); font-style: italic; font-weight: 700; font-size: 20px; text-decoration: none; }
  .merit-badge {
    position: absolute; left: 64px; top: 445px; width: 96px; height: 144px;
    background: var(--badge); border-radius: 4px;
  }
  .leaf-mark {
    position: absolute; left: 58px; top: 633px; width: 108px; height: 44px; border-radius: 22px;
    background: linear-gradient(90deg, #b97a23, #f0c46a, #b97a23);
  }

  .welcome-title { left: 394px; top: 1104px; color: var(--ink-navy); font-weight: 900; font-size: 31px; letter-spacing: 0.2px; white-space: nowrap; }
  .body-copy { font-size: 15px; line-height: 16.3px; color: var(--text); font-weight: 700; }
  .copy-a { left: 394px; top: 1180px; width: 334px; }
  .copy-b { left: 394px; top: 1284px; width: 334px; }
  .copy-c { left: 394px; top: 1572px; width: 656px; }
  .portrait {
    left: 751px; top: 1182px; width: 279px; height: 362px;
    background: linear-gradient(180deg, #c9a566 0%, #b68f52 40%, #2a2622 55%, #141210 100%);
  }
  .cta { left: 394px; width: 666px; text-align: center; color: var(--ink-navy); font-style: italic; font-weight: 900; font-size: 30px; text-decoration: none; }
  .cta-gallery { top: 1700px; }
  .cta-pedigree { top: 1762px; }

  .site-footer { left: 0; top: 1895px; width: 1200px; height: 327px; background: var(--night); text-align: center; }
  .footer-line { position: absolute; left: 0; width: 100%; color: var(--pale); font-weight: 700; font-size: 18px; }
  .footer-contact { top: 36px; }
  .footer-copy { top: 121px; }
  .footer-leaf {
    position: absolute; left: 547px; top: 68px; width: 106px; height: 44px; border-radius: 22px;
    background: linear-gradient(90deg, #b97a23, #f0c46a, #b97a23);
  }
  .banner-slot {
    position: absolute; left: 287px; top: 181px; width: 624px; height: 77px;
    background: var(--sky); border: 1px solid #9fb8c4;
    display: flex; align-items: center; justify-content: center;
    font-weight: 900; font-size: 18px; color: var(--ink-navy); letter-spacing: 0.5px;
  }
</style>
</head>
<body>

  <div class="abs top-strip"></div>
  <header class="abs hero" role="img" aria-label="Marsh at dawn with cattails, a retriever silhouette and flying ducks"></header>
  <div class="abs brand">Birchfall Kennels</div>

  <nav class="abs main-nav">
    <a href="#" style="left:304px">HOME</a>
    <a href="#" style="left:449px">PIP'S PEDIGREE</a>
    <a href="#" style="left:627px">TRIAL RESULTS</a>
    <a href="#" style="left:775px">GALLERY</a>
    <a href="#" style="left:887px">CONTACT</a>
  </nav>

  <section class="abs slider"></section>
  <div class="abs slide-photo" role="img" aria-label="Black Labrador retriever leaping through splashing water in a field"></div>
  <svg class="abs slide-arrow" style="left:140px" width="32" height="52" viewBox="0 0 32 52"><polyline points="26,4 6,26 26,48" fill="none" stroke="var(--arrow)" stroke-width="5"/></svg>
  <svg class="abs slide-arrow" style="left:1026px" width="32" height="52" viewBox="0 0 32 52"><polyline points="6,4 26,26 6,48" fill="none" stroke="var(--arrow)" stroke-width="5"/></svg>

  <section class="abs intro">
    <div class="intro-kicker">INTRODUCING</div>
    <div class="intro-title">HRCH Pip's Whistle 4 Rounds MH</div>
    <div class="intro-note">(Available at Stud to approved bitches)</div>
  </section>

  <main class="abs content"></main>

  <aside class="abs sidebar">
    <div class="sidebar-title">ANNOUNCEMENTS</div>
    <div class="announcements">
      <p>11-11-17:&nbsp; New Champion, HRCH Pip's Whistle 4 Rounds MH</p>
      <p>11-11-17:&nbsp; New Champion, HRCH Pip's Whistle 4 Rounds MH</p>
      <p>11-11-17:&nbsp; Puppies confirmed, due December 7, 17.</p>
    </div>
    <div class="contact-art" role="img" aria-label="Flying geese illustration"></div>
    <a class="contact-link" href="#">Contact Us</a>
    <div class="merit-badge" role="img" aria-label="Breeder certification badge"></div>
    <div class="leaf-mark" role="img" aria-label="Oak leaf and acorn ornament"></div>
  </aside>

  <h1 class="abs welcome-title">WELCOME TO BIRCHFALL KENNELS</h1>
  <p class="abs body-copy copy-a">This is the home of one Pip; one phenomenal dog.&nbsp; Please look through our site - read the trial results and view his pedigree.&nbsp; All his ducks are in a row and he is now available at stud.</p>
  <p class="abs body-copy copy-b">Write some more about Pip here. Lorem ipsum dolor sit amet, consetetur sadipscing elitr, sed diam nonumy eirmod tempor invidunt ut labore et dolore magna aliquyam erat, sed diam voluptua. At vero eos et accusam et justo duo dolores et ea rebum. Stet clita kasd gubergren, no sea takimata sanctus est Lorem ipsum dolor sit amet. Lorem ipsum dolor sit amet, consetetur sadipscing elitr, sed diam nonumy eirmod tempor invidunt ut labore et dolore magna aliquyam erat, sed diam voluptua. At vero eos et accusam et justo duo dolores et ea rebum.</p>
  <div class="abs portrait" role="img" aria-label="Portrait of a black Labrador retriever in golden grass"></div>
  <p class="abs body-copy copy-c">Duis autem vel eum iriure dolor in hendrerit in vulputate velit esse molestie consequat, vel illum dolore eu feugiat nulla facilisis at vero eros et accumsan et iusto odio dignissim qui blandit praesent luptatum zzril delenit augue duis dolore te feugait nulla facilisi. Lorem ipsum dolor sit amet, consectetuer adipiscing elit, sed diam nonummy nibh euismod tincidunt ut laoreet dolore magna aliquam erat volutpat.</p>
  <a class="abs cta cta-gallery" href="#">Visit Pip's Gallery</a>
  <a class="abs cta cta-pedigree" href="http://www.fieldpupregistry.example/pedigree.asp?id=71926">View Our Boy's Pedigree</a>

  <footer class="abs site-footer">
    <div class="footer-line footer-contact">Name, Address, Email, Phone</div>
    <div class="footer-leaf" role="img" aria-label="Oak leaf and acorn ornament"></div>
    <div class="footer-line footer-copy">Copyright 2017 Birchfall Kennels</div>
    <div class="banner-slot">BANNER</div>
  </footer>

</body>
</html>
```